The Garden Under the Lantern: A Quiet Pilgrimage

This is a memoir about my breakdown/breakthrough followed by a spiritual awakening in 2012, I found my guru Hemant Sulori Dev, Mother Ayahuasca, and my spiritual mother, Lalu. By 2013, I was headed for a spiritual adventure through India, Southeast India, and Nepal which lasted 14 months. I lived in ashrams, meditated and prayed in temples,, traveled by train and bus, met many enlightened beings and interesting people. During Vipassana, I discovered my true essence- the light of my soul. It is a book of travel, romance, and spiritual growth. My idea is a road lined with temples, etc. I am walking down the road and see myself at the end of the road, facing out, with a bright star in my heart center. I see the colors in muted yellows and other earth-tone hues. Marigolds are used everywhere in the temples to adorn statues and doorways and this speaks to me. The title of the book is about finding out who I am beyond my stories and it is also about how our story will reveal to us who we really are.

Target Market(s)

Spiritual seekers, adventurers, travelers

Industry/Entity Type

Spiritual

Font styles to use
Serif
Sans Serif
Other font styles liked:
• I’m open. I like simplicity

Colors
FFC000
F8CF3A
FAE287
FDF2CF
FEFAEE

Requirements
Must have
• My name: Greta Lunara Ses, Earth tones, pastels, me or a likeness of me, room for ISBN on back cover
Nice to have
• In the photo uploads I drew an idea of what I would like, there is also the idea in the book
Should not have
• I am not a fan of bright colors and that's all I can select here. I like neutral colors, like browns, slate, creams, and whites. This reflects the dusty roads I took throughout my journey.

```html
<!DOCTYPE html>
<html lang="en">
<head>
<meta charset="UTF-8">
<title>The Garden Under the Lantern — Cover</title>
<link rel="stylesheet" href="https://fonts.googleapis.com/css2?family=Cormorant+Garamond:ital,wght@0,400;0,500;1,400;1,500&display=swap">
<style>
  :root {
    --backdrop: #262626;
    --paper: #f3f3ec;
    --gold: #d4c48f;
    --slate: #a3a3a3;
    --figure-top: #dfded3;
    --figure-bottom: #ebe7dc;
  }
  * { margin: 0; padding: 0; box-sizing: border-box; }
  html, body {
    width: 1200px;
    height: 1200px;
    overflow: hidden;
    background: var(--backdrop);
  }
  .cover {
    position: absolute;
    left: 217px;
    top: 26px;
    width: 765px;
    height: 1148px;
    background: var(--paper);
    overflow: hidden;
    font-family: "Cormorant Garamond", "Times New Roman", serif;
    color: var(--gold);
  }
  .cover__figure {
    position: absolute;
    left: 323px;
    top: 448px;
    width: 118px;
    height: 700px;
    border-radius: 50px 50px 10px 10px;
    background: linear-gradient(to bottom, var(--figure-top) 0%, var(--figure-top) 55%, var(--figure-bottom) 100%);
  }
  .title-line {
    position: absolute;
    left: 0;
    width: 100%;
    text-align: center;
    line-height: 1;
    font-size: 112px;
    font-weight: 400;
    letter-spacing: 0.1em;
    white-space: nowrap;
  }
  .title-line--1 { top: 130px; }
  .title-line--2 { top: 332px; font-style: italic; letter-spacing: 0.08em; }
  .title-line--3 { top: 536px; }
  .title-line--4 { top: 740px; }
  .subtitle {
    position: absolute;
    left: 0;
    top: 954px;
    width: 100%;
    text-align: center;
    font-size: 38px;
    font-style: italic;
    line-height: 1;
    letter-spacing: 0.18em;
    color: var(--slate);
  }
  .author {
    position: absolute;
    left: 0;
    top: 1080px;
    width: 100%;
    text-align: center;
    font-size: 27px;
    line-height: 1;
    letter-spacing: 0.06em;
    text-transform: uppercase;
  }
</style>
</head>
<body>
  <main class="cover">
    <div class="cover__figure" role="img" aria-label="Soft silhouette of a woman walking away, with her faint reflection below"></div>
    <h1 class="cover__title">
      <span class="title-line title-line--1">The Garden</span>
      <span class="title-line title-line--2">Under</span>
      <span class="title-line title-line--3">The</span>
      <span class="title-line title-line--4">Lantern</span>
    </h1>
    <p class="subtitle">A Quiet Pilgrimage</p>
    <p class="author">Greta Lunara Ses</p>
  </main>
</body>
</html>
```